I am a business consultant/coach and I am branding myself 'The Zero Fee Venture Mentor'. My business name is Bright Harbor Advisory.I want an oversized postcard designed for lead generation. It will be sent through the post so will require area for an address and stamp The details that I want on the card are attached plus a photo of myself. Also I have attached a copy of my business card so that you are able to see the style and colors I use. I would like the main headline to be bold red, or bold red background Hope this is enough info.
Target Market(s)
Owners/managers of medium sized businesses
Industry/Entity Type
Business Consultant
Requirements
Must have
- The cards I want to be noticed and professional in appearance, they will be use dfor lead generation and sent through the postal service
Nice to have
- The colors that I use on my business cards are green, grey and white. I want the main headline to be in red or red backgroun dso that it stands out
Should not have
- The words that I have used are basically off my landing page for consistency

```html
<!DOCTYPE html>
<html lang="en">
<head>
<meta charset="utf-8">
<title>Bright Harbor Advisory – Lead Generation Postcard</title>
<link rel="stylesheet" href="https://fonts.googleapis.com/css2?family=Lato:ital,wght@0,400;0,700;0,900;1,400;1,700&family=Oswald:wght@500;600&family=Roboto+Condensed:wght@400;700&display=swap">
<style>
  :root {
    --red: #e4252b;
    --red-dark: #c81d22;
    --green: #8cc63f;
    --green-light: #b5d96b;
    --grey-dark: #4a4a4c;
    --grey-mid: #8a8a8a;
    --grey-light: #e4e4e4;
    --white: #ffffff;
    --ink: #222222;
    --page: #eeeeec;
    --photo-cool: #c9ced4;
    --photo-warm: #d9b9a2;
  }
  * { box-sizing: border-box; margin: 0; padding: 0; }
  html, body { width: 825px; height: 1200px; overflow: hidden; background: var(--page); }
  body { position: relative; font-family: "Lato", Arial, sans-serif; color: var(--ink); }

  .card { position: absolute; left: 123px; width: 581px; background: var(--white); overflow: hidden; box-shadow: 0 2px 6px rgba(0,0,0,.18); }
  .card--front { top: 118px; height: 448px; }
  .card--back { top: 633px; height: 450px; }

  .shapes { position: absolute; inset: 0; width: 100%; height: 100%; }

  .brand { position: absolute; left: 30px; top: 26px; font-family: "Lato", sans-serif; font-weight: 900; font-size: 25px; color: var(--grey-dark); letter-spacing: -.5px; }

  .headline { position: absolute; right: 18px; top: 20px; text-align: right; color: var(--white); }
  .headline__lead { font-family: "Oswald", sans-serif; font-weight: 600; font-size: 14.5px; letter-spacing: .1px; line-height: 1.2; }
  .headline__sub { font-family: "Roboto Condensed", sans-serif; font-size: 17.5px; line-height: 1.25; }

  .intro { position: absolute; right: 126px; top: 114px; text-align: right; font-style: italic; font-size: 13px; line-height: 1.18; color: var(--ink); }
  .portrait { position: absolute; border: 2px solid var(--red); background: linear-gradient(180deg, var(--photo-cool) 0%, var(--photo-warm) 55%, #f4f4f4 100%); }
  .card--front .portrait { left: 470px; top: 99px; width: 84px; height: 110px; }
  .call { font-family: "Oswald", sans-serif; font-weight: 500; color: var(--red); text-transform: uppercase; }
  .card--front .call { position: absolute; left: 267px; top: 176px; font-size: 19px; }

  .offer { position: absolute; right: 22px; top: 242px; text-align: right; font-style: italic; font-weight: 700; color: var(--ink); }
  .offer__question { font-size: 12.5px; line-height: 1.3; }
  .offer__note { font-size: 10.5px; margin-top: 1px; }

  .explainer { position: absolute; left: 24px; right: 24px; top: 332px; text-align: center; font-style: italic; font-size: 9.6px; line-height: 1.45; color: #444; }

  .contact-bar { position: absolute; left: 0; right: 0; bottom: 0; height: 45px; background: var(--grey-dark); border-top: 5px solid var(--red); color: var(--white); font-family: "Roboto Condensed", sans-serif; font-size: 14.5px; display: flex; align-items: center; justify-content: center; }

  .back-panel { position: absolute; left: 0; top: 0; width: 281px; height: 450px; }
  .back-intro { position: absolute; left: 27px; top: 26px; width: 240px; font-style: italic; font-size: 10px; line-height: 1.3; color: #555; }
  .promise { position: absolute; left: 27px; top: 133px; width: 240px; color: var(--white); }
  .promise__title { font-weight: 900; font-size: 17px; line-height: 1.1; }
  .promise__text { font-style: italic; font-size: 10.5px; line-height: 1.3; margin-top: 2px; }
  .card--back .portrait { left: 27px; top: 253px; width: 73px; height: 94px; }
  .back-intro-name { position: absolute; left: 114px; top: 267px; font-style: italic; font-size: 11.5px; line-height: 1.18; color: var(--ink); }
  .card--back .call { position: absolute; left: 114px; top: 315px; font-size: 14.5px; }

  .stamp { position: absolute; left: 501px; top: 30px; width: 55px; height: 55px; background: #c8c8c8; }
</style>
</head>
<body>

<section class="card card--front" aria-label="Postcard front">
  <svg class="shapes" viewBox="0 0 581 448" aria-hidden="true">
    <defs>
      <linearGradient id="greyFade" x1="0" y1="0" x2="0" y2="1">
        <stop offset="0" stop-color="#ffffff"/><stop offset="1" stop-color="#d8d8d8"/>
      </linearGradient>
      <linearGradient id="greenFade" x1="0" y1="0" x2="0" y2="1">
        <stop offset="0" stop-color="#9dcb45"/><stop offset="1" stop-color="#c5df86"/>
      </linearGradient>
      <linearGradient id="bodyFade" x1="0" y1="0" x2="0" y2="1">
        <stop offset="0" stop-color="#ffffff"/><stop offset="1" stop-color="#dcdcdc"/>
      </linearGradient>
    </defs>
    <rect x="0" y="304" width="581" height="94" fill="url(#bodyFade)"/>
    <rect x="0" y="79" width="581" height="148" fill="url(#greyFade)"/>
    <polygon points="172,0 182,0 215,79 205,79" fill="#9a9a9a"/>
    <polygon points="182,0 581,0 581,79 215,79" fill="var(--red)"/>
    <rect x="0" y="79" width="581" height="4" fill="var(--green)"/>
    <polygon points="232,227 581,227 581,304 200,304" fill="url(#greenFade)"/>
    <polygon points="0,83 210,83 250,152 200,304 0,304" fill="var(--green)"/>
    <polygon points="0,83 198,83 238,152 190,304 0,304" fill="var(--red)"/>
  </svg>
  <div role="img" aria-label="Photo of hands working at a laptop with printed charts"
       style="position:absolute;left:0;top:83px;width:240px;height:221px;clip-path:polygon(0 0,194px 0,234px 69px,186px 221px,0 221px);background:linear-gradient(135deg,#e9eaec 0%,#c4c7cc 45%,#9ea2a8 75%,#d3d5d8 100%);"></div>

  <div class="brand">brightharbor</div>

  <div class="headline">
    <p class="headline__lead">Has Your Business Achieved The Outcomes You Want?</p>
    <p class="headline__sub">It can and I’m prepared to show you how</p>
  </div>

  <p class="intro">My name is Daniel Whitmore,<br>from Bright Harbor Advisory,<br>the ‘Zero Fee Venture Mentor’.</p>
  <div class="portrait" role="img" aria-label="Portrait photo of the consultant"></div>
  <p class="call">Call me on 0412 555 018</p>

  <div class="offer">
    <p class="offer__question">If I told you that you can increase your profits, give yourself<br>more time, freedom and peace, what would your answer be…?</p>
    <p class="offer__note">Research says you can and quickly</p>
  </div>

  <p class="explainer">Because over 90 percent of small to medium sized business in Australia have a minimum of 12 per cent of their annual turnover tied up in ineffective &amp; inefficient processes? The problem is that most business owners focus on their daily challenges unable to free themselves to consider where the ‘hidden profit’ may be locked up within their business.</p>

  <div class="contact-bar">If you would like more information go to brightharbor.com.au/zerofee or email hello@brightharbor.com.au</div>
</section>

<section class="card card--back" aria-label="Postcard back">
  <svg class="shapes" viewBox="0 0 581 450" aria-hidden="true">
    <defs>
      <linearGradient id="backGrey" x1="0" y1="0" x2="0" y2="1">
        <stop offset="0" stop-color="#e2e2e2"/><stop offset="1" stop-color="#ffffff"/>
      </linearGradient>
      <linearGradient id="backGreen" x1="0" y1="0" x2="0" y2="1">
        <stop offset="0" stop-color="#b9dc6e"/><stop offset="1" stop-color="#8cc63f"/>
      </linearGradient>
    </defs>
    <rect x="0" y="0" width="281" height="105" fill="url(#backGrey)"/>
    <polygon points="0,98 140,90 281,98 281,112 140,104 0,112" fill="var(--grey-dark)"/>
    <polygon points="0,112 140,104 281,112 281,227 0,227" fill="var(--red)"/>
    <rect x="275" y="0" width="6" height="227" fill="var(--red)"/>
    <rect x="0" y="232" width="281" height="4" fill="var(--grey-dark)"/>
    <rect x="0" y="236" width="281" height="134" fill="url(#backGreen)"/>
    <rect x="0" y="370" width="73" height="80" fill="var(--green)"/>
  </svg>

  <p class="back-intro">I can change this by reviewing your cashflow, systems, staff capability, business culture and Risk. The end result will be more money, time, freedom and peace to live your life that way you desire.</p>

  <div class="promise">
    <p class="promise__title">MY PROMISE:</p>
    <p class="promise__text">If I cannot uncover at least 5 times my fee from potential profits hidden with your business after one interview then it is free.</p>
  </div>

  <div class="portrait" role="img" aria-label="Portrait photo of the consultant"></div>
  <p class="back-intro-name">My name is Daniel Whitmore,<br>from Bright Harbor Advisory,<br>the ‘Zero Fee Venture Mentor’.</p>
  <p class="call">Call me on 0412 555 018</p>

  <div class="stamp" aria-label="Stamp area"></div>
</section>

</body>
</html>
```